TCH Business cards

We are a medium sized property company based in London and require a logo, Business card which reflects a professional company and incorporates our catchy name.

Our statement is (Building for the future) we like colours such as royal blue, greens and light browns but will look at anything.

Contact Information for Business Card

Tidecrest Holdings Limited
Unit 4, 3-5 Parbrook Lane
London
SE21 7QX

Web: www.tidecrestholdings.example

Email: tidecrestltd@mailbox.example

Telephone: +44-208-555-0142
Fax: +44-208-555-0187

```html
<!DOCTYPE html>
<html lang="en">
<head>
<meta charset="utf-8">
<title>Tidecrest Holdings – Business Card</title>
<link rel="stylesheet" href="https://fonts.googleapis.com/css2?family=Audiowide&display=swap">
<style>
  :root {
    --lime: #a4f43c;
    --lime-dark: #8fd92e;
    --white: #ffffff;
    --card-w: 1200px;
    --card-h: 791px;
  }
  html, body {
    margin: 0;
    padding: 0;
    overflow: hidden;
    background: var(--white);
  }
  .card {
    position: relative;
    width: var(--card-w);
    height: var(--card-h);
    background: var(--white);
    overflow: hidden;
    font-family: "Audiowide", sans-serif;
  }
  .brand {
    position: absolute;
    top: 120px;
    left: 0;
    width: 100%;
    display: flex;
    justify-content: center;
    align-items: center;
    gap: 28px;
  }
  .brand__mark {
    width: 70px;
    height: 70px;
    background: var(--lime);
  }
  .brand__name {
    font-size: 96px;
    line-height: 1;
    color: var(--lime);
  }
  .panel {
    position: absolute;
    left: 0;
    top: 366px;
    width: 100%;
    height: calc(var(--card-h) - 366px);
    background: var(--lime);
  }
  .panel__edge {
    position: absolute;
    left: 0;
    top: 356px;
    width: 100%;
    height: 6px;
    background: repeating-linear-gradient(90deg, var(--lime) 0 12px, transparent 12px 18px);
  }
  .company {
    position: absolute;
    top: 372px;
    left: 0;
    width: 100%;
    text-align: center;
    font-size: 37px;
    color: var(--white);
    letter-spacing: 0.5px;
    margin: 0;
    font-weight: 400;
  }
  .contacts {
    position: absolute;
    left: 38px;
    top: 488px;
    margin: 0;
    padding: 0;
    list-style: none;
  }
  .contacts__item {
    display: flex;
    align-items: center;
    height: 40px;
    margin-bottom: 14px;
    font-size: 29px;
    color: var(--white);
    white-space: pre;
  }
  .contacts__item--address { margin-bottom: 15px; }
  .contacts__item--phone { margin-bottom: 19px; }
  .contacts__item--fax { margin-bottom: 11px; }
  .contacts__icon {
    width: 40px;
    height: 36px;
    margin-right: 20px;
    flex: none;
  }
</style>
</head>
<body>
<main class="card">
  <div class="brand">
    <span class="brand__mark"></span>
    <span class="brand__name">Tidecrest</span>
  </div>

  <div class="panel__edge"></div>
  <section class="panel"></section>

  <h1 class="company">Tidecrest Holdings Ltd .</h1>

  <ul class="contacts">
    <li class="contacts__item contacts__item--address">
      <svg class="contacts__icon" viewBox="0 0 40 36" aria-hidden="true">
        <path d="M8 30 L10 22 L28 4 L34 10 L16 28 Z" fill="none" stroke="#fff" stroke-width="3" stroke-linejoin="round"/>
        <path d="M10 22 L16 28" stroke="#fff" stroke-width="3"/>
      </svg>Unit 4  3-5  Parbrook Lane  London, SE21 7QX</li>
    <li class="contacts__item contacts__item--phone">
      <svg class="contacts__icon" viewBox="0 0 40 36" aria-hidden="true">
        <path d="M4 8 Q20 0 36 8 L34 13 L28 11 L28 8 L12 8 L12 11 L6 13 Z" fill="#fff"/>
        <rect x="8" y="14" width="24" height="20" rx="2" fill="#fff"/>
        <g fill="var(--lime)">
          <rect x="12" y="18" width="4" height="3"/><rect x="18" y="18" width="4" height="3"/><rect x="24" y="18" width="4" height="3"/>
          <rect x="12" y="23" width="4" height="3"/><rect x="18" y="23" width="4" height="3"/><rect x="24" y="23" width="4" height="3"/>
          <rect x="12" y="28" width="4" height="3"/><rect x="18" y="28" width="4" height="3"/><rect x="24" y="28" width="4" height="3"/>
        </g>
      </svg>+44  208  555  0142</li>
    <li class="contacts__item contacts__item--fax">
      <svg class="contacts__icon" viewBox="0 0 40 36" aria-hidden="true">
        <rect x="11" y="2" width="18" height="10" fill="#fff"/>
        <rect x="4" y="12" width="32" height="14" rx="3" fill="#fff"/>
        <rect x="11" y="21" width="18" height="13" fill="#fff" stroke="var(--lime)" stroke-width="2"/>
        <circle cx="31" cy="17" r="1.8" fill="var(--lime)"/>
      </svg>+44  208  555  0187</li>
    <li class="contacts__item contacts__item--email">
      <svg class="contacts__icon" viewBox="0 0 40 36" aria-hidden="true">
        <rect x="4" y="8" width="32" height="21" fill="none" stroke="#fff" stroke-width="3"/>
        <path d="M4 8 L20 21 L36 8 M4 29 L16 18 M36 29 L24 18" fill="none" stroke="#fff" stroke-width="2.5"/>
      </svg>tidecrestltd@mailbox.example</li>
    <li class="contacts__item contacts__item--web">
      <svg class="contacts__icon" viewBox="0 0 40 36" aria-hidden="true">
        <circle cx="20" cy="18" r="14" fill="none" stroke="#fff" stroke-width="3"/>
        <ellipse cx="20" cy="18" rx="6" ry="14" fill="none" stroke="#fff" stroke-width="2"/>
        <path d="M6 18 H34 M9 11 H31 M9 25 H31" stroke="#fff" stroke-width="2"/>
      </svg>tidecrestholdings.example</li>
  </ul>
</main>
</body>
</html>
```